1 Page Sales Brochure of our Services

I need to create a one page brochure that our sales team can take into meetings about our services - Need this to be an impressive one page that looks fresh and new using our brand colors of Brindle green, black and white. Our brand looks "clean" think Marlo brand in how everything is clean and white and crisp. Our website showcases our services: https://brindlesports.example/services/ --- After done with this project I would like to create a full booklet. Want to begin with this project first.

Target Market(s)

State of Texas

Industry/Entity Type

Sports Construction in Texas Only

Font styles to use
Serif

Colors
00AB8E
00BBA5
67D7C9
C6EFE9
E9F9F6

Requirements
Must have
• Front and Back and cover our services outlined on our website: https://brindlesports.example/services/
Nice to have
• Need one that can get sent digital and printed -- Our colors are the Brindle green, white and black - We want brochure to look clean, almost like the Marlo feel of their product's branding

```html
<!DOCTYPE html>
<html lang="en">
<head>
<meta charset="utf-8">
<title>Brindle Sports Construction – Services Brochure</title>
<link rel="stylesheet" href="https://fonts.googleapis.com/css2?family=Bebas+Neue&family=Poppins:wght@400;500;600;700&display=swap">
<style>
:root{
  --green:#137b32;
  --green-dark:#0e6428;
  --black:#000;
  --white:#fff;
  --ink:#1a1a1a;
  --rule:#a8a8a8;
  --stage:#e4e4e4;
}
*{margin:0;padding:0;box-sizing:border-box}
html,body{width:1200px;height:2909px;overflow:hidden}
body{background:var(--stage);font-family:"Poppins",sans-serif;color:var(--ink);position:relative}
.page{position:absolute;left:141px;width:919px;background:var(--white);overflow:hidden}
.page-front{top:105px;height:1300px}
.page-back{top:1491px;height:1299px}
.abs{position:absolute}
.display{font-family:"Bebas Neue",sans-serif;font-weight:400;line-height:1}

.brand-name{left:0;width:919px;top:50px;text-align:center;font-family:"Poppins",sans-serif;font-weight:600;font-size:66px;color:var(--green);letter-spacing:1px}
.brand-name .dot{display:inline-block;width:18px;height:18px;border-radius:50%;background:var(--green);margin-right:14px;vertical-align:middle}

.hero-rule{left:376px;top:188px;width:543px;height:7px;background:var(--green)}
.photo{background:linear-gradient(135deg,#b9b4a8,#d9cfb8 45%,#8c9a7a)}
.hero-photo{left:376px;top:195px;width:543px;height:320px}
.hero-panel{left:0;top:221px;width:376px;height:294px;background:var(--black);color:var(--white)}
.hero-title{left:45px;top:30px;font-size:53px;color:var(--white)}
.hero-title span{color:var(--green)}
.hero-bar{left:45px;top:136px;width:72px;height:3px;background:var(--green)}
.hero-text{left:45px;top:149px;width:310px;font-size:12.4px;line-height:1.18}
.tag-band{left:0;top:515px;width:919px;height:55px;background:var(--green);text-align:center;font-weight:700;font-size:26px;line-height:55px;color:var(--white);letter-spacing:-.2px}
.tag-band span{color:var(--black)}

.section-title{left:45px;font-size:44px;color:var(--black)}
.section-rule{left:45px;width:796px;height:3px;background:var(--rule)}

.svc-photo{width:232px;height:151px;border-top:5px solid var(--green);border-left:5px solid var(--green);border-radius:14px}
.svc-title{font-size:30px;color:var(--black)}
.svc-title::after{content:"";display:block;width:60px;height:3px;background:var(--green);margin-top:3px}
.svc-text{font-size:12.4px;line-height:1.2;color:var(--ink)}
.svc-sub{font-size:15.5px;font-weight:600;color:var(--black)}

.photo-track{background:linear-gradient(160deg,#9fb6c9,#3f8b3a 45%,#b4453a)}
.photo-grass{background:linear-gradient(180deg,#5d8fd8,#a9c6ea 55%,#4e7c2c 62%,#6d9a3e)}
.photo-synthetic{background:linear-gradient(135deg,#e58a2c,#6d6a62 50%,#9b958a)}
.photo-stadium{background:linear-gradient(135deg,#a7a49a,#6f8f4e 50%,#b99a7d)}
.photo-tennis{background:linear-gradient(180deg,#5ea0e6,#2d5a2a 50%,#2474c6 75%,#3b8a3a)}
.photo-maint{background:linear-gradient(180deg,#c7d3dc,#3c8a2c 35%,#1f6a22)}
.photo-light{background:linear-gradient(90deg,#6f7a4f,#47552f 50%,#2b5a2b 52%,#58a64a)}
.photo-surface{background:linear-gradient(180deg,#c9d6e3,#7a8d6a 35%,#6b2c8a 60%,#d9d2ea)}

.quote{left:52px;top:1100px;width:800px;font-size:16.5px;line-height:1.22;font-weight:500;color:var(--black)}
.quote .mark{position:absolute;left:0;top:-4px;font-family:"Poppins",sans-serif;font-weight:700;font-size:26px}
.quote p{padding-left:22px}
.quote .close{font-weight:700;font-size:22px;vertical-align:-4px}
.quote cite{display:block;padding-left:22px;margin-top:6px;font-style:normal;font-weight:700;font-size:16px}

.footer{left:0;width:919px;height:108px}
.footer-shape{position:absolute;left:0;top:0}
.icon{flex:none;display:block}
.f-call{left:44px;top:36px;font-size:19px;font-weight:600;color:var(--white)}
.f-phone{left:165px;top:33px;font-family:"Bebas Neue",sans-serif;font-size:27px;line-height:1.2;color:var(--white);display:flex;align-items:center;gap:9px}
.f-web{left:354px;top:26px;font-size:12.6px;line-height:1.55;color:var(--white)}
.f-web div{display:flex;align-items:center;gap:6px}
.f-addr{left:610px;top:29px;font-size:12.3px;line-height:1.2;color:var(--white);display:flex;align-items:flex-start;gap:9px}
.f-addr .icon{margin-top:1px}
</style>
</head>
<body>

<section class="page page-front">
  <div class="abs brand-name"><span class="dot"></span>Brindle</div>

  <div class="abs hero-rule"></div>
  <div class="abs photo hero-photo" role="img" aria-label="Aerial view of a stadium track under construction with graded sand infield"></div>
  <div class="abs hero-panel">
    <h1 class="abs display hero-title">Building <span>to a</span><br>Higher Standard</h1>
    <div class="abs hero-bar"></div>
    <p class="abs hero-text">Since 2010, Brindle Sports Construction has been on the cutting edge of sports construction and design. Founded by Marcus T. Hale, we are one of the largest, most respected sports construction companies in the nation. Our client rapport and satisfaction rate speaks to the quality, integrity, and timely completion you can expect by partnering with us.</p>
  </div>
  <div class="abs tag-band">TURNKEY SOLUTIONS FOR <span>SPORTS CONSTRUCTION</span></div>

  <h2 class="abs display section-title" style="top:597px">Services</h2>
  <div class="abs section-rule" style="top:641px"></div>

  <div class="abs photo svc-photo photo-track" style="left:47px;top:664px" role="img" aria-label="Aerial photo of a football field surrounded by a running track"></div>
  <h3 class="abs display svc-title" style="left:300px;top:666px">Track Construction</h3>
  <p class="abs svc-text" style="left:300px;top:704px;width:560px">When you're looking to have a track installed at your school or facility, there are many factors that come into play. This is a highly specialized job, and you'll want to work with a team that has the expertise necessary to plan and execute a quality installation. At Brindle, we are proud to offer solutions in track construction for a variety of client types. Brindle recommends the Stridelane line of running track systems developed by Pavetec, owned by Arena Group, as the industry leaders in high quality, performance-enhancing systems that result in unmatched results for the lifecycle of your track.</p>

  <h3 class="abs display svc-title" style="left:47px;top:849px">Natural Grass Fields</h3>
  <p class="abs svc-text" style="left:47px;top:890px;width:560px">Natural Grass is a growing area of our business and we have brought in natural grass experts to join the Brindle team who understand the challenges involved with installing and maintaining grass fields. Two of our experts are certified field builders with one specializing in both synthetic and natural grass installations. Our team operates with specialized equipment allowing massive amounts of dirt to be moved and graded when building natural grass fields.</p>
  <div class="abs photo svc-photo photo-grass" style="left:640px;top:849px" role="img" aria-label="Natural grass baseball outfield under a blue sky"></div>

  <div class="abs photo svc-photo photo-synthetic" style="left:47px;top:1013px" role="img" aria-label="Worker installing synthetic turf with a seaming machine"></div>
  <h3 class="abs display svc-title" style="left:300px;top:1010px">Synthetic Field Construction</h3>
  <p class="abs svc-sub" style="left:300px;top:1049px">The Right TerraTurf System for Every Venue</p>
  <p class="abs svc-text" style="left:300px;top:1074px;width:562px">With the wide selection of synthetic turf systems– no matter the venue or sport– Brindle has a viable solution.<br>TerraTurf's premium turf system series boasts heavy face weights for the best the industry has to offer in aesthetics, durability, and player protection. These systems are driven by the latest research, and technology pushing the industry towards the most grass-like surfaces available</p>

  <div class="abs footer" style="top:1192px">
    <svg class="footer-shape" width="919" height="108" viewBox="0 0 919 108" aria-hidden="true">
      <rect x="571" y="26" width="348" height="39" fill="var(--green)"/>
      <polygon points="0,0 571,0 614,108 0,108" fill="var(--black)"/>
    </svg>
    <div class="abs f-call">Call us at</div>
    <div class="abs f-phone"><svg class="icon" width="20" height="20" viewBox="0 0 24 24" aria-hidden="true"><path fill="#fff" d="M6.6 10.8a15.1 15.1 0 0 0 6.6 6.6l2.2-2.2c.3-.3.7-.4 1-.2 1.1.4 2.3.6 3.6.6.6 0 1 .4 1 1V20c0 .6-.4 1-1 1C10.6 21 3 13.4 3 4c0-.6.4-1 1-1h3.5c.6 0 1 .4 1 1 0 1.3.2 2.5.6 3.6.1.3 0 .7-.2 1z"/></svg><span>(555) 010 4821</span></div>
    <div class="abs f-web">
      <div><svg class="icon" width="13" height="10" viewBox="0 0 13 10" aria-hidden="true"><rect width="13" height="10" fill="#fff"/><path d="M0 0l6.5 5L13 0" stroke="#000" fill="none"/></svg><span>info@brindlesports.example</span></div>
      <div><svg class="icon" width="13" height="13" viewBox="0 0 14 14" aria-hidden="true"><circle cx="7" cy="7" r="6" fill="none" stroke="#fff" stroke-width="1.4"/><ellipse cx="7" cy="7" rx="2.6" ry="6" fill="none" stroke="#fff" stroke-width="1.2"/><path d="M1 7h12" stroke="#fff" stroke-width="1.2"/></svg><span>www.brindlesports.example</span></div>
    </div>
    <div class="abs f-addr"><svg class="icon" width="13" height="16" viewBox="0 0 12 16" aria-hidden="true"><path d="M6 1a4.5 4.5 0 0 0-4.5 4.5C1.5 9 6 14 6 14s4.5-5 4.5-8.5A4.5 4.5 0 0 0 6 1z" fill="none" stroke="#fff" stroke-width="1.5"/><circle cx="6" cy="5.5" r="1.5" fill="#fff"/><path d="M2 15h8" stroke="#fff" stroke-width="1.3"/></svg><div>48 Cedar Row Street<br>Pinefield, Texas 75000</div></div>
  </div>
</section>

<section class="page page-back">
  <h2 class="abs display section-title" style="top:69px">Services</h2>
  <div class="abs section-rule" style="top:114px"></div>

  <div class="abs photo svc-photo photo-stadium" style="left:47px;top:157px" role="img" aria-label="Aerial view of a completed high school stadium"></div>
  <h3 class="abs display svc-title" style="left:300px;top:155px">Stadium Construction</h3>
  <p class="abs svc-text" style="left:300px;top:196px;width:562px">In every sense of the word, Brindle is a one-stop shop for all things sports construction. We are a true turn-key construction company owned and operated by seasoned professionals who care. From ground-up stadium construction to total lifecycle planning, we provide custom construction solutions through all stages of your projects.</p>

  <h3 class="abs display svc-title" style="left:47px;top:357px">Tennis Court Construction</h3>
  <p class="abs svc-text" style="left:47px;top:399px;width:560px">To ensure that our customers are playing on the best tennis courts available, we've partnered with Pavetec to provide Courtline court surfacing systems. Courtline offers a variety of impact reducing, performance enhancing court systems that are of the highest quality in the industry. Learn more about why Courtline is the top choice for tennis court construction, and contact us to get started on your tennis court project today.</p>
  <div class="abs photo svc-photo photo-tennis" style="left:640px;top:360px" role="img" aria-label="Blue tennis courts lined with tall pine trees"></div>

  <div class="abs photo svc-photo photo-maint" style="left:47px;top:522px" role="img" aria-label="Technician kneeling to inspect synthetic turf on a field"></div>
  <h3 class="abs display svc-title" style="left:300px;top:519px">Service + Maintenance</h3>
  <p class="abs svc-text" style="left:300px;top:560px;width:562px">Brindle Sports is here to support you throughout the entire lifecycle of your sports construction projects from conception to intermittent servicing when needed. We provide maintenance services and support for all sports surfaces, helping you protect your investment and extend the life of your synthetic turf, track or tennis court through education, performance testing, and maintenance services. It's important to us that each customer gets the most out of their sports surfaces, that peak performance, safety, and ease of maintenance are a part of the customer experience. That is our ongoing commitment to you.</p>

  <h3 class="abs display svc-title" style="left:47px;top:721px">Stadium Lighting</h3>
  <p class="abs svc-text" style="left:47px;top:763px;width:560px">Brindle also provides lighting services. Take advantage of the energy efficiency and cost savings by converting to LED lighting. According to the US Department of Energy, light-emitting diodes (LED) are six to seven times more energy efficient than conventional light bulbs and cut energy use by more than 80 percent. LED light bulbs can also last 25,000 hours or more, which is 25 times longer than traditional bulbs. You can see why LED lighting makes financial sense!</p>
  <div class="abs photo svc-photo photo-light" style="left:640px;top:723px" role="img" aria-label="Before and after aerial comparison of a field under old and new LED lighting"></div>

  <div class="abs photo svc-photo photo-surface" style="left:47px;top:923px" role="img" aria-label="Grooming machine driving over a purple synthetic end zone"></div>
  <h3 class="abs display svc-title" style="left:300px;top:920px">Surface Maintenance + Repair</h3>
  <p class="abs svc-text" style="left:300px;top:961px;width:562px">All sports systems involve some component of maintenance to ensure your surface is performing properly and will withstand the test of time. Many of our synthetic fields undergo annual field maintenance and bacterial and COVID killing sprays. This is particularly important for athletes who will be using indoor facilities as they do not receive sunlight which aids in killing bacteria. If you would like to have a free maintenance or field/surface evaluation, please email us at aftercare@brindlesports.example.</p>

  <blockquote class="abs quote">
    <span class="mark">&ldquo;</span>
    <p>Cedar Ridge isd chose brindle sports to install the highest quality product on the market. We love our product and this professional, honest, and dependable company. <span class="close">&rdquo;</span></p>
    <cite>— dale morgan, superintendent, cedar ridge isd</cite>
  </blockquote>

  <div class="abs footer" style="top:1191px">
    <svg class="footer-shape" width="919" height="108" viewBox="0 0 919 108" aria-hidden="true">
      <rect x="571" y="26" width="348" height="39" fill="var(--green)"/>
      <polygon points="0,0 571,0 614,108 0,108" fill="var(--black)"/>
    </svg>
    <div class="abs f-call">Call us at</div>
    <div class="abs f-phone"><svg class="icon" width="20" height="20" viewBox="0 0 24 24" aria-hidden="true"><path fill="#fff" d="M6.6 10.8a15.1 15.1 0 0 0 6.6 6.6l2.2-2.2c.3-.3.7-.4 1-.2 1.1.4 2.3.6 3.6.6.6 0 1 .4 1 1V20c0 .6-.4 1-1 1C10.6 21 3 13.4 3 4c0-.6.4-1 1-1h3.5c.6 0 1 .4 1 1 0 1.3.2 2.5.6 3.6.1.3 0 .7-.2 1z"/></svg><span>(555) 010 4821</span></div>
    <div class="abs f-web">
      <div><svg class="icon" width="13" height="10" viewBox="0 0 13 10" aria-hidden="true"><rect width="13" height="10" fill="#fff"/><path d="M0 0l6.5 5L13 0" stroke="#000" fill="none"/></svg><span>info@brindlesports.example</span></div>
      <div><svg class="icon" width="13" height="13" viewBox="0 0 14 14" aria-hidden="true"><circle cx="7" cy="7" r="6" fill="none" stroke="#fff" stroke-width="1.4"/><ellipse cx="7" cy="7" rx="2.6" ry="6" fill="none" stroke="#fff" stroke-width="1.2"/><path d="M1 7h12" stroke="#fff" stroke-width="1.2"/></svg><span>www.brindlesports.example</span></div>
    </div>
    <div class="abs f-addr"><svg class="icon" width="13" height="16" viewBox="0 0 12 16" aria-hidden="true"><path d="M6 1a4.5 4.5 0 0 0-4.5 4.5C1.5 9 6 14 6 14s4.5-5 4.5-8.5A4.5 4.5 0 0 0 6 1z" fill="none" stroke="#fff" stroke-width="1.5"/><circle cx="6" cy="5.5" r="1.5" fill="#fff"/><path d="M2 15h8" stroke="#fff" stroke-width="1.3"/></svg><div>48 Cedar Row Street<br>Pinefield, Texas 75000</div></div>
  </div>
</section>

</body>
</html>
```